Print and E-book Personal Injury Front and Back Book Cover

I need a book cover for a personal injury law firm book titled "Rising Past the Wreckage" with the subtitle "A Plain Guide for Harmed Readers." The book cover should have an image. This isas a lead generation book designed to be give to potential clients to have them sign as new clients.

Target Market(s)

Potential New Clients Looking For a Personal Injury Attorney

Industry/Entity Type

Legal

Requirements
Must have
• Title and some type of image or images

```html
<!DOCTYPE html>
<html lang="en">
<head>
<meta charset="utf-8">
<title>Rising Past the Wreckage – Cover Wrap</title>
<link rel="stylesheet" href="https://fonts.googleapis.com/css2?family=Abril+Fatface&family=Oswald:wght@600&family=Libre+Baskerville:wght@700&family=Open+Sans:wght@400&display=swap">
<style>
  :root {
    --stage: #2a2a2a;
    --yellow: #f9dc4a;
    --ink: #0b0b0b;
    --photo-light: #d9d9d9;
    --photo-mid: #8a8a8a;
    --photo-dark: #262626;
  }
  * { margin: 0; padding: 0; box-sizing: border-box; }
  html, body {
    width: 1200px; height: 288px; overflow: hidden;
    background: var(--stage);
  }
  .cover-wrap {
    position: absolute; left: 389px; top: 0;
    width: 421px; height: 288px;
    display: flex;
  }
  .panel { position: relative; height: 288px; overflow: hidden; }

  /* Back cover */
  .back-cover { width: 98px; background: var(--ink); color: var(--yellow); }
  .back-title { position: absolute; left: 10px; top: 43px; width: 78px; height: 42px; }
  .back-title text { font-family: "Abril Fatface", serif; fill: var(--yellow); }
  .blurb {
    position: absolute; left: 13px; width: 74px;
    font-family: "Open Sans", sans-serif; font-size: 5.1px; line-height: 7.5px;
    text-align: justify; text-align-last: center;
  }
  .back-cover .blurb { top: 93px; height: 168px; overflow: hidden; }
  .blurb p + p { margin-top: 7.5px; }

  /* Inside flap */
  .flap { width: 94px; background: var(--yellow); color: var(--ink); }
  .author-portrait {
    position: absolute; left: 16px; top: 44px; width: 62px; height: 55px;
    background: radial-gradient(ellipse at 50% 60%, #b9a89a 0%, #e9e6e2 55%, #ffffff 100%);
  }
  .flap .blurb { left: 10px; top: 107px; width: 74px; height: 150px; overflow: hidden; }

  /* Spine */
  .spine { width: 36px; background: var(--ink); color: var(--yellow); }
  .spine-title, .spine-author {
    position: absolute; left: 50%; transform: translateX(-50%);
    writing-mode: vertical-rl; white-space: nowrap;
    font-family: "Libre Baskerville", serif; font-weight: 700;
  }
  .spine-title { top: 19px; font-size: 9.6px; letter-spacing: 0.2px; }
  .spine-author { top: 210px; font-size: 8px; }

  /* Front cover */
  .front-cover { width: 193px; background: var(--yellow); }
  .front-title { position: absolute; left: 0; top: 10px; width: 193px; height: 100px; }
  .front-title .title-line { font-family: "Abril Fatface", serif; fill: var(--ink); }
  .front-title .subtitle { font-family: "Oswald", sans-serif; font-weight: 600; fill: var(--ink); }
  .cover-photo {
    position: absolute; left: 0; top: 110px; width: 193px; height: 142px;
    background:
      radial-gradient(circle at 78% 52%, var(--photo-light) 0%, var(--photo-mid) 22%, transparent 34%),
      linear-gradient(100deg, var(--photo-dark) 0%, #5c5c5c 35%, #b5b5b5 60%, #6e6e6e 100%);
  }
  .front-author {
    position: absolute; left: 0; right: 0; top: 262px;
    text-align: center;
    font-family: "Libre Baskerville", serif; font-weight: 700;
    font-size: 10.5px; color: var(--ink); letter-spacing: 0.2px;
  }
</style>
</head>
<body>
  <main class="cover-wrap">
    <section class="panel back-cover">
      <svg class="back-title" viewBox="0 0 78 42" aria-label="Rising Past the Wreckage">
        <text x="39" y="15" text-anchor="middle" font-size="17" textLength="66" lengthAdjust="spacingAndGlyphs">RISING</text>
        <text x="39" y="28" text-anchor="middle" font-size="13" textLength="58" lengthAdjust="spacingAndGlyphs">PAST THE</text>
        <text x="39" y="40" text-anchor="middle" font-size="11.5" textLength="76" lengthAdjust="spacingAndGlyphs">WRECKAGE</text>
      </svg>
      <div class="blurb">
        <p>Lorem ipsum dolor sit amet, consectetur adipiscing elit, sed do eiusmod tempor incididunt ut labore et dolore magna aliqua. Quis ipsum suspendisse ultrices gravida. Risus commodo viverra maecenas accumsan lacus vel facilisis. Lorem ipsum dolor sit amet, consectetur adipiscing elit, sed do eiusmod tempor incididunt ut labore et dolore magna aliqua. Quis ipsum suspendisse ultrices gravida. Risus commodo viverra maecenas accumsan lacus vel facilisis.</p>
        <p>Lorem ipsum dolor sit amet, consectetur adipiscing elit, sed do eiusmod tempor incididunt ut labore et dolore magna aliqua. Quis ipsum suspendisse ultrices</p>
      </div>
    </section>

    <section class="panel flap">
      <div class="author-portrait" role="img" aria-label="Author portrait photograph"></div>
      <div class="blurb">
        <p>Lorem ipsum dolor sit amet, consectetur adipiscing elit, sed do eiusmod tempor incididunt ut labore et dolore magna aliqua. Quis ipsum suspendisse ultrices gravida. Risus commodo viverra maecenas accumsan lacus vel facilisis. Lorem ipsum dolor sit amet, consectetur adipiscing elit, sed do eiusmod tempor incididunt ut labore et dolore magna aliqua. Quis ipsum suspendisse ultrices gravida. Risus commodo viverra maecenas accumsan lacus vel facilisis.</p>
        <p>Lorem ipsum dolor sit amet, consectetur adipiscing elit, sed do eiusmod tempor incididunt ut</p>
      </div>
    </section>

    <section class="panel spine">
      <div class="spine-title">RISING PAST THE WRECKAGE</div>
      <div class="spine-author">AUTHOR NAME</div>
    </section>

    <section class="panel front-cover">
      <svg class="front-title" viewBox="0 0 193 100" aria-label="Rising Past the Wreckage: A Plain Guide for Harmed Readers">
        <text class="title-line" x="96.5" y="37" text-anchor="middle" font-size="40" textLength="148" lengthAdjust="spacingAndGlyphs">RISING</text>
        <text class="title-line" x="96.5" y="62" text-anchor="middle" font-size="27" textLength="122" lengthAdjust="spacingAndGlyphs">PAST THE</text>
        <text class="title-line" x="96.5" y="84" text-anchor="middle" font-size="22" textLength="148" lengthAdjust="spacingAndGlyphs">WRECKAGE</text>
        <text class="subtitle" x="96.5" y="97" text-anchor="middle" font-size="9" textLength="168" lengthAdjust="spacingAndGlyphs">A PLAIN GUIDE FOR HARMED READERS</text>
      </svg>
      <div class="cover-photo" role="img" aria-label="Black and white photograph of a Lady Justice statue holding scales beside law books and a globe in front of window blinds"></div>
      <div class="front-author">AUTHOR NAME</div>
    </section>
  </main>
</body>
</html>
```